PICTURE CALENDAR - CONSTRUCTION COMPANY

- PICTURES CALENDAR 2018 (wall calendar) - graphic design - square 50 x 50 cm - 14 pages (title - months index pages) - languages ​​- german - Italian - construction industry - minimalistic and clear - modern - for each month inkluding logo color www.peltronbau.it

Reason: Sehr geehrte Damen und Herren, bitte um eine Fristverlängerung. Es ist Wochenende und ich selbst bekomme auf kein Feedback ob ein Design jetzt passt oder nicht. Weiters haben wir bereits einen Favoriten welcher aber noch Details abändern müsste. Vielen Dank! Mit freundlichen Grüßen, Matthias Grübel

Target Market(s)

construction worker

Industry/Entity Type

Construction

Font styles to use
Sans Serif

Colors
0355a3
dddddd

Requirements
Must have
• 49 x 49 cm 12 months german italiano short image description including logo
Nice to have
• cool line
Should not have
• the graphic design not playful, no gradients

```html
<!DOCTYPE html>
<html lang="en">
<head>
<meta charset="utf-8">
<title>Peltron Bau – Wall Calendar 2018 – September</title>
<link rel="stylesheet" href="https://fonts.googleapis.com/css2?family=Arimo:wght@700&family=Open+Sans:wght@400;600;700&display=swap">
<style>
  :root {
    --brand-blue: #0355a3;
    --light-blue: #2f77bd;
    --weekend-grey: #f2f2f2;
    --rule-grey: #9a9a9a;
    --ink: #111111;
    --paper: #ffffff;
    --photo-sky: #c6d4e2;
    --photo-ground: #a49d91;
  }
  html, body {
    margin: 0;
    width: 1200px;
    height: 1200px;
    overflow: hidden;
    background: var(--paper);
  }
  .canvas {
    position: relative;
    width: 1200px;
    height: 1200px;
    overflow: hidden;
  }
  .page {
    position: absolute;
    top: 0;
    left: 0;
    width: 1417px;
    height: 1417px;
    transform: scale(0.84686);
    transform-origin: 0 0;
    background: var(--paper);
    font-family: "Open Sans", Arial, sans-serif;
  }
  .artwork {
    position: absolute;
    inset: 0;
    width: 1417px;
    height: 1417px;
  }
  .caption {
    position: absolute;
    left: 22px;
    top: 183px;
    margin: 0;
    color: var(--paper);
    font-size: 27px;
    font-weight: 400;
    letter-spacing: 0.2px;
    white-space: nowrap;
  }
  .title {
    position: absolute;
    right: 22px;
    top: 515px;
    margin: 0;
    text-align: right;
    font-family: "Arimo", Arial, sans-serif;
    font-weight: 700;
    line-height: 1;
  }
  .title-year {
    display: block;
    color: var(--light-blue);
    font-size: 112px;
  }
  .title-month {
    display: block;
    margin-top: 10px;
    color: var(--brand-blue);
    font-size: 124px;
    letter-spacing: -1px;
  }
  .month-grid {
    position: absolute;
    left: 473px;
    top: 826px;
    width: 923px;
    height: 540px;
    display: grid;
    grid-template-columns: repeat(7, 1fr);
    grid-template-rows: 32px repeat(5, 102px);
    column-gap: 0;
  }
  .weekend-column {
    position: absolute;
    top: 826px;
    width: 132px;
    height: 540px;
    background: var(--weekend-grey);
  }
  .weekend-sun { left: 473px; }
  .weekend-sat { left: 1264px; }
  .weekday {
    margin: 0 6px 0 8px;
    border-bottom: 1.5px solid var(--rule-grey);
    color: var(--brand-blue);
    font-size: 28px;
    font-weight: 600;
    line-height: 32px;
    padding-left: 0;
  }
  .day {
    margin: 0 6px 0 5px;
    border-bottom: 1.5px solid var(--rule-grey);
    color: var(--ink);
    font-size: 31px;
    font-weight: 600;
    padding: 4px 0 0 6px;
  }
  .week-last .day, .day.week-last { border-bottom: none; }
  .brand {
    position: absolute;
    left: 25px;
    top: 1250px;
    display: flex;
    align-items: center;
    gap: 14px;
  }
  .brand-mark {
    width: 78px;
    height: 78px;
    background: var(--brand-blue);
  }
  .brand-name {
    color: var(--brand-blue);
    font-size: 38px;
    font-weight: 700;
    letter-spacing: -0.5px;
  }
  .web-address {
    position: absolute;
    left: 22px;
    top: 1350px;
    margin: 0;
    color: var(--paper);
    font-size: 31px;
    font-weight: 700;
    line-height: 44px;
  }
</style>
</head>
<body>
<div class="canvas">
  <div class="page">
    <svg class="artwork" viewBox="0 0 1417 1417" xmlns="http://www.w3.org/2000/svg">
      <defs>
        <linearGradient id="photo-tone" x1="0" y1="0" x2="0" y2="1">
          <stop offset="0" stop-color="#c6d4e2"/>
          <stop offset="0.45" stop-color="#d6dce2"/>
          <stop offset="1" stop-color="#a49d91"/>
        </linearGradient>
      </defs>
      <polygon class="photo-area" role="img"
        aria-label="Photo: orange long-reach excavator working on a slope of crushed stone under a cloudy blue sky"
        points="0,0 1020,0 1265,195 0,1160" fill="url(#photo-tone)"/>
      <polygon class="stripe-light" points="1028,0 1062,0 1318,200 0,1188 0,1162 1268,197" fill="#2f77bd"/>
      <polygon class="stripe-dark" points="1085,0 1417,0 1417,175 0,1218 0,1196 1342,200" fill="#0355a3"/>
      <polygon class="caption-band" points="0,178 1172,178 1100,234 0,234" fill="#2f77bd" fill-opacity="0.85"/>
      <polygon class="web-band" points="0,1348 340,1348 365,1417 0,1417" fill="#0355a3"/>
      <rect class="footer-band" x="0" y="1396" width="1417" height="21" fill="#0355a3"/>
    </svg>

    <p class="caption">Lorem ipsum dolor sit amet, consectetur adipiscing elit, sed do eiusmod tempor</p>

    <h1 class="title">
      <span class="title-year">2018</span>
      <span class="title-month">September</span>
    </h1>

    <div class="weekend-column weekend-sun"></div>
    <div class="weekend-column weekend-sat"></div>

    <div class="month-grid">
      <div class="weekday">Sun</div><div class="weekday">Mon</div><div class="weekday">Tue</div><div class="weekday">Wed</div><div class="weekday">Thu</div><div class="weekday">Fri</div><div class="weekday">Sat</div>

      <div class="day">30</div><div class="day"></div><div class="day"></div><div class="day"></div><div class="day"></div><div class="day"></div><div class="day">&nbsp;1</div>
      <div class="day">2</div><div class="day">&nbsp;3</div><div class="day">&nbsp;4</div><div class="day">5</div><div class="day">6</div><div class="day">7</div><div class="day">8</div>
      <div class="day">9</div><div class="day">10</div><div class="day">11</div><div class="day">12</div><div class="day">13</div><div class="day">14</div><div class="day">15</div>
      <div class="day">16</div><div class="day">17</div><div class="day">18</div><div class="day">19</div><div class="day">20</div><div class="day">21</div><div class="day">22</div>
      <div class="day week-last">23</div><div class="day week-last">24</div><div class="day week-last">25</div><div class="day week-last">26</div><div class="day week-last">27</div><div class="day week-last">28</div><div class="day week-last">29</div>
    </div>

    <div class="brand">
      <div class="brand-mark"></div>
      <span class="brand-name">peltron bau</span>
    </div>

    <p class="web-address">www.peltronbau.it</p>
  </div>
</div>
</body>
</html>
```